Website front page and logo re-designed (using logo provided)

We are looking for the home page of our new website. It is a website offering a space for clients to ask professionals questions. The website should be similar in design to www.quibblenest.com however it is clear it should be a different look. It should be modern, simple to use, a clear navigation bar at the top and bottom.

Logo should be similar to the one attached, but more professional and modern. Logo should be clearly incorporated into website. Design should focus on our website colours as in the logo.

Logo Text

KnowHive - Truth with every reply!

Number of Pages Required

1 page

Font styles to use
Sans Serif

```html
<!DOCTYPE html>
<html lang="en">
<head>
<meta charset="utf-8">
<title>KnowHive – Truth with every reply!</title>
<link rel="stylesheet" href="https://fonts.googleapis.com/css2?family=Raleway:wght@400;500;600;700&family=Open+Sans:ital,wght@0,400;0,600;0,700;1,400&display=swap">
<style>
:root{
  --green:#2e8b1c;
  --green-dark:#246f14;
  --green-light:#8fd07a;
  --red:#d4232a;
  --orange:#f7a21b;
  --ink:#333;
  --line:#d6d6d6;
  --star:#f29a1d;
}
*{margin:0;padding:0;box-sizing:border-box}
html,body{width:1200px;height:2350px;overflow:hidden}
body{font-family:"Open Sans",Arial,sans-serif;color:var(--ink);background:#fff;position:relative}
h1,h2,h4{font-weight:400}
.abs{position:absolute}

/* hero */
.hero{left:0;top:0;width:1200px;height:545px;background:radial-gradient(ellipse at 50% 30%,#ffffff 0%,#f3f3f3 60%,#dcdcdc 100%)}
.hero-photo{left:517px;top:78px;width:556px;height:467px;background:linear-gradient(160deg,#e9e9e9 0%,#d7dde2 45%,#bfcbd4 100%)}
.brand{left:185px;top:26px}
.brand-name{font-family:"Raleway",sans-serif;font-weight:700;font-size:40px;color:var(--green);line-height:1}
.brand-tag{font-family:"Raleway",sans-serif;font-weight:600;font-size:12px;color:#222;margin-left:22px;margin-top:2px}
.nav{left:564px;top:39px;display:flex;gap:24px;font-family:"Raleway",sans-serif;font-size:15px;color:#555}
.btn-signup{left:871px;top:34px;width:72px;height:30px;background:var(--green);color:#fff;font-family:"Raleway",sans-serif;font-size:12px;text-align:center;line-height:30px}
.btn-login{left:948px;top:34px;width:70px;height:30px;background:var(--orange);color:#fff;font-family:"Raleway",sans-serif;font-size:12px;text-align:center;line-height:30px}
.hero-kicker{left:185px;top:155px;font-family:"Raleway",sans-serif;font-size:26px;color:#444}
.hero-title{left:185px;top:186px;font-family:"Raleway",sans-serif;font-size:31px;color:#222;font-weight:500}
.ask-box{left:183px;top:240px;width:481px;height:225px;background:var(--green)}
.ask-tabs{left:22px;top:13px;display:flex;gap:14px;font-family:"Raleway",sans-serif;font-size:12.5px;color:#fff}
.ask-input{left:22px;top:58px;width:437px;height:102px;background:#fff;font-size:12px;color:#777;padding:16px 14px}
.ask-btn{left:22px;top:170px;width:177px;height:37px;background:var(--red);color:#fff;font-family:"Raleway",sans-serif;font-size:16px;text-align:center;line-height:37px;font-weight:500}
.dots{left:556px;top:514px;display:flex;gap:5px}
.dots span{width:16px;height:16px;border-radius:50%;background:#fff;border:1px solid #ccc}
.dots span.on{background:#e8b600;border-color:#fff}

/* why */
.section-title{width:1200px;left:0;text-align:center;font-family:"Raleway",sans-serif;font-weight:400}
.why-title{top:588px;font-size:33px;color:var(--red)}
.why-intro{left:240px;top:640px;width:720px;text-align:center;font-size:12.5px;line-height:21px;color:#666}
.feature{width:390px;height:80px}
.feature-icon{left:0;top:0;width:78px;height:78px;border-radius:50%;border:2px solid var(--line);display:flex;align-items:center;justify-content:center}
.feature-name{left:88px;top:6px;font-family:"Raleway",sans-serif;font-size:17px;color:#444}
.feature-text{left:88px;top:32px;width:300px;font-size:11px;line-height:19px;color:#777}

/* services */
.services{left:0;top:976px;width:1200px;height:334px;background:linear-gradient(100deg,#c9262a 0%,#e0392f 50%,#cf2c2a 100%)}
.services-title{top:1003px;font-size:27px;color:#fff}
.service-card{top:1056px;width:256px;height:207px;border:2px solid #fff;color:#fff;text-align:center}
.service-card svg{margin-top:44px}
.service-name{margin-top:14px;font-family:"Raleway",sans-serif;font-weight:600;font-size:16px;letter-spacing:.3px}
.service-text{margin:8px auto 0;width:190px;font-size:11px;line-height:16px}

/* partners */
.partners{left:0;top:1310px;width:1200px;height:81px;background:linear-gradient(#fafafa,#e8e8e8);border-bottom:1px solid #d5d5d5}
.partner{top:1336px;height:30px;background:#bdbdbd}

/* recent */
.recent-title{top:1440px;font-size:26px;color:#444}
.q-row{left:251px;width:700px;height:22px;font-size:12.5px;color:#444}
.q-row b{font-weight:700;color:#333}
.q-stars{left:457px;top:3px}
.q-time{left:579px;top:0;font-size:12px;color:#555}

/* testimonials */
.testimonials{left:0;top:1770px;width:1200px;height:317px;background:linear-gradient(100deg,#3a3a3a 0%,#262626 50%,#1f1f1f 100%)}
.testi-title{top:1808px;font-size:28px;color:#fff}
.avatar{left:560px;top:1861px;width:70px;height:70px;border-radius:50%;border:3px solid #fff;background:linear-gradient(#c9a98a,#8a6d58)}
.quote{left:270px;top:1942px;width:660px;text-align:center;font-style:italic;font-size:13px;line-height:22px;color:#fff}
.quote-mark{font-family:Georgia,serif;font-style:normal;font-size:44px;line-height:0;position:relative;color:#fff}
.quote-mark.open{top:6px;margin-right:6px}
.quote-mark.close{top:22px;margin-left:6px}
.author{top:2020px;font-weight:600;font-size:15px;color:#fff;font-family:"Open Sans",sans-serif}

/* footer */
.footer{left:0;top:2087px;width:1200px;height:205px;background:var(--green)}
.footer-brand{left:182px;top:2150px}
.footer-brand .brand-name{color:var(--green-light);font-size:36px}
.footer-brand .brand-tag{color:var(--green-light);font-size:11px;margin-left:20px}
.footer-col{top:2130px}
.footer-col h4{font-family:"Raleway",sans-serif;font-weight:500;font-size:15px;color:#fff;margin-bottom:8px}
.footer-col li{list-style:none;font-size:11px;color:#fff;line-height:21px}
.social{display:flex;gap:4px;margin-top:4px}
.social span{width:29px;height:29px;border-radius:50%;border:1.5px solid #fff}
.bottom-bar{left:0;top:2292px;width:1200px;height:58px;background:var(--green-dark)}
.copyright{left:194px;top:2313px;font-size:11px;color:#e8f3e4}
</style>
</head>
<body>

<header class="abs hero"></header>
<div class="abs hero-photo" role="img" aria-label="Photo of a doctor in a white coat holding a blue tablet"></div>

<div class="abs brand">
  <div class="brand-name">KnowHive</div>
  <div class="brand-tag">Truth with every reply!</div>
</div>
<nav class="abs nav"><span>Features</span><span>How it works</span><span>Ask Question</span></nav>
<div class="abs btn-signup">Sign Up</div>
<div class="abs btn-login">Log In</div>

<div class="abs hero-kicker">Do you want to Ask a Question</div>
<h1 class="abs hero-title">Get an Answer Now</h1>

<div class="abs ask-box">
  <div class="abs ask-tabs"><span>Lawyer</span><span>Doctor</span><span>IT Computer</span><span>Education</span><span>Merchants</span><span>More Categories</span></div>
  <div class="abs ask-input">Type question here</div>
  <div class="abs ask-btn">Get an Answer</div>
</div>
<div class="abs dots"><span class="on"></span><span></span><span></span><span></span></div>

<h2 class="abs section-title why-title">Why Choose KnowHive</h2>
<p class="abs why-intro">Morbi diam mauris viverra in gravida eu mattis in ante Morbi eget arcu Morbi porta libero id ullamcorper nonummy nibh ligula pulvinar metus eget consectetuer augue nisi quis lacus Ut ac mi quis lacus mollis aliquam</p>

<div class="abs feature" style="left:196px;top:727px">
  <div class="abs feature-icon"><svg width="30" height="30" viewBox="0 0 30 30"><circle cx="15" cy="9" r="6" fill="#888"/><path d="M4 28c0-7 5-11 11-11s11 4 11 11z" fill="#888"/></svg></div>
  <div class="abs feature-name">One to One</div>
  <div class="abs feature-text">viverra in gravida eu mattis in ante Morbi eget arcu Morbi porta libero id ullamcorper nonu</div>
</div>
<div class="abs feature" style="left:611px;top:727px">
  <div class="abs feature-icon"><svg width="32" height="32" viewBox="0 0 32 32"><path d="M29 3 3 14l9 4 3 10 4-7 7 4z" fill="#888"/><path d="M12 18 29 3 15 22" fill="#666"/></svg></div>
  <div class="abs feature-name">Convenience</div>
  <div class="abs feature-text">viverra in gravida eu mattis in ante Morbi eget arcu Morbi porta libero id ullamcorper nonu</div>
</div>
<div class="abs feature" style="left:196px;top:834px">
  <div class="abs feature-icon"><svg width="34" height="30" viewBox="0 0 34 30"><ellipse cx="14" cy="11" rx="12" ry="8" fill="none" stroke="#888" stroke-width="3"/><path d="M6 17 4 24l8-5" fill="#888"/><path d="M24 8c6 1 9 4 9 8s-3 6-6 7l2 5-7-4" fill="none" stroke="#888" stroke-width="3"/></svg></div>
  <div class="abs feature-name">24/7 Availability</div>
  <div class="abs feature-text">viverra in gravida eu mattis in ante Morbi eget arcu Morbi porta libero id ullamcorper nonu</div>
</div>
<div class="abs feature" style="left:611px;top:834px">
  <div class="abs feature-icon"><svg width="38" height="30" viewBox="0 0 38 30"><circle cx="19" cy="8" r="5" fill="#888"/><circle cx="8" cy="11" r="4" fill="#888"/><circle cx="30" cy="11" r="4" fill="#888"/><path d="M10 28c0-8 4-12 9-12s9 4 9 12z" fill="#888"/><path d="M1 26c0-6 3-9 7-9 2 0 3 1 3 1-2 2-3 5-3 8z" fill="#888"/><path d="M37 26c0-6-3-9-7-9-2 0-3 1-3 1 2 2 3 5 3 8z" fill="#888"/></svg></div>
  <div class="abs feature-name">Million People Joined</div>
  <div class="abs feature-text">viverra in gravida eu mattis in ante Morbi eget arcu Morbi porta libero id ullamcorper nonu</div>
</div>

<section class="abs services" role="img" aria-label="Red-tinted photo of people working on laptops in a library"></section>
<h2 class="abs section-title services-title">Services Provide</h2>
<div class="abs service-card" style="left:191px">
  <svg width="48" height="40" viewBox="0 0 48 40"><rect x="8" y="4" width="32" height="22" rx="2" fill="none" stroke="#fff" stroke-width="3"/><path d="M2 31h44l-3 5H5z" fill="#fff"/></svg>
  <div class="service-name">INSTANT ANSWER</div>
  <p class="service-text">neque at volutpat rutrum purus nisi eleifend libero a tempus libero</p>
</div>
<div class="abs service-card" style="left:472px">
  <svg width="48" height="40" viewBox="0 0 48 40"><circle cx="24" cy="20" r="17" fill="none" stroke="#fff" stroke-width="4"/><path d="M24 10v11h8" fill="none" stroke="#fff" stroke-width="4"/></svg>
  <div class="service-name">100% SATISFACTION</div>
  <p class="service-text">neque at volutpat rutrum purus nisi eleifend libero a tempus libero</p>
</div>
<div class="abs service-card" style="left:754px">
  <svg width="48" height="40" viewBox="0 0 48 40"><circle cx="24" cy="20" r="19" fill="#fff"/><path d="M15 20l7 7 12-13" fill="none" stroke="#d4232a" stroke-width="5"/></svg>
  <div class="service-name">GET STARTED</div>
  <p class="service-text">neque at volutpat rutrum purus nisi eleifend libero a tempus libero</p>
</div>

<div class="abs partners"></div>
<div class="abs partner" style="left:226px;width:56px"></div>
<div class="abs partner" style="left:327px;width:96px"></div>
<div class="abs partner" style="left:472px;width:90px"></div>
<div class="abs partner" style="left:608px;width:92px"></div>
<div class="abs partner" style="left:770px;width:68px"></div>
<div class="abs partner" style="left:898px;width:96px"></div>

<h2 class="abs section-title recent-title">Recent Asked Question</h2>
<svg width="0" height="0" style="position:absolute">
  <defs>
    <path id="star" d="M6 0l1.8 3.8 4.2.5-3.1 2.9.8 4.1L6 9.3 2.3 11.3l.8-4.1L0 4.3l4.2-.5z"/>
  </defs>
</svg>

<div class="abs q-row" style="top:1506px"><b>Q:</b> Pellentesque faucibus Ut accumsan ultricies elit Maecenas
  <svg class="abs q-stars" width="72" height="12"><use href="#star" x="0" fill="#f29a1d"/><use href="#star" x="14" fill="#f29a1d"/><use href="#star" x="28" fill="#f29a1d"/><use href="#star" x="42" fill="#f29a1d"/><use href="#star" x="56" fill="#f29a1d"/></svg>
  <span class="abs q-time">2 hours ago</span></div>
<div class="abs q-row" style="top:1540px"><b>Q:</b> At justo id velit placerat molestie Donec dictum
  <svg class="abs q-stars" width="72" height="12"><use href="#star" x="0" fill="#f29a1d"/><use href="#star" x="14" fill="#f29a1d"/><use href="#star" x="28" fill="#f29a1d"/><use href="#star" x="42" fill="#f29a1d"/><use href="#star" x="56" fill="#bbb"/></svg>
  <span class="abs q-time">5 hours ago</span></div>
<div class="abs q-row" style="top:1573px"><b>Q:</b> Cras a ante vitae enim iaculis aliquam Mauris nunc quam venenatis
  <svg class="abs q-stars" width="72" height="12"><use href="#star" x="0" fill="#f29a1d"/><use href="#star" x="14" fill="#f29a1d"/><use href="#star" x="28" fill="#f29a1d"/><use href="#star" x="42" fill="#f29a1d"/><use href="#star" x="56" fill="#bbb"/></svg>
  <span class="abs q-time">8 hours ago</span></div>
<div class="abs q-row" style="top:1607px"><b>Q:</b> Pellentesque habitant morbi tristique senectus et
  <svg class="abs q-stars" width="72" height="12"><use href="#star" x="0" fill="#f29a1d"/><use href="#star" x="14" fill="#f29a1d"/><use href="#star" x="28" fill="#f29a1d"/><use href="#star" x="42" fill="#f29a1d"/><use href="#star" x="56" fill="#bbb"/></svg>
  <span class="abs q-time">1 day ago</span></div>
<div class="abs q-row" style="top:1640px"><b>Q:</b> Aetus et malesuada fames ac turpis egestas Cras id elit
  <svg class="abs q-stars" width="72" height="12"><use href="#star" x="0" fill="#f29a1d"/><use href="#star" x="14" fill="#f29a1d"/><use href="#star" x="28" fill="#f29a1d"/><use href="#star" x="42" fill="#f29a1d"/><use href="#star" x="56" fill="#bbb"/></svg>
  <span class="abs q-time">1 day ago</span></div>
<div class="abs q-row" style="top:1674px"><b>Q:</b> Integer quis urna Ut ante enim dapibus malesuada fringilla
  <svg class="abs q-stars" width="72" height="12"><use href="#star" x="0" fill="#f29a1d"/><use href="#star" x="14" fill="#f29a1d"/><use href="#star" x="28" fill="#f29a1d"/><use href="#star" x="42" fill="#f29a1d"/><use href="#star" x="56" fill="#f29a1d"/></svg>
  <span class="abs q-time">1 day ago</span></div>

<section class="abs testimonials" role="img" aria-label="Dark photo of a man smiling at a laptop"></section>
<h2 class="abs section-title testi-title">Testimonials</h2>
<div class="abs avatar" role="img" aria-label="Portrait of the reviewer"></div>
<p class="abs quote"><span class="quote-mark open">&ldquo;</span>Mauris vel lacus vitae felis vestibulum volutpat imperdiet ac nisl Cum sociis natoque penatibus et magnis dis parturient montes nascetur ridiculus mus In iaculis facilisis massa Etiam eu urna Sed porta Suspendisse quam leo molestie sed luctus quis feugiat in pede Fusce tellus Sed metus augue convallis<span class="quote-mark close">&rdquo;</span></p>
<div class="abs section-title author">By Author Name</div>

<footer class="abs footer"></footer>
<div class="abs footer-brand">
  <div class="brand-name">KnowHive</div>
  <div class="brand-tag">Truth with every reply!</div>
</div>
<div class="abs footer-col" style="left:423px"><h4>COMPANY</h4><ul><li>Home</li><li>About Us</li><li>Testimonials</li><li>Blog Post</li></ul></div>
<div class="abs footer-col" style="left:556px"><h4>SERVICES</h4><ul><li>Donec dictum</li><li>Lectus non odio</li><li>Enim iaculis</li><li>Aliquam Mauris</li></ul></div>
<div class="abs footer-col" style="left:717px"><h4>RESOURCES</h4><ul><li>Support</li><li>News</li><li>Contact Us</li></ul></div>
<div class="abs footer-col" style="left:866px;top:2126px"><h4>FOLLOW US</h4><div class="social"><span></span><span></span><span></span><span></span></div></div>
<div class="abs bottom-bar"></div>
<div class="abs copyright">© 2016 Company Name &nbsp;All right reserved &nbsp;Term of Use</div>

</body>
</html>
```